Need sign/billboard help

I need somone to take my logo and turn it into a sign.
Needs to have: Bright Paws
Hound Play Lodge LLC
319-555-0187
Daycare - Boarding - Learning
Colors to use are in the pictures i included, however feel free to use different shades of gray. i Don't necessary want to background to be one solid color.
Also this sing will be a rectangle (4'x8')
Industry/Entity Type
Daycare
Look and feel
Each slider illustrates characteristics of the customer's brand and the style your logo design should communicate.

```html
<!DOCTYPE html>
<html lang="en">
<head>
<meta charset="utf-8">
<title>Bright Paws – Hound Play Lodge LLC Sign</title>
<link href="https://fonts.googleapis.com/css2?family=Arimo:wght@700&family=Roboto+Condensed:wght@700&display=swap" rel="stylesheet">
<style>
  :root {
    --page: #ffffff;
    --lime: #a2d800;
    --ink: #0b0b0b;
    --slate: #53646c;
    --white: #ffffff;
  }
  html, body {
    margin: 0;
    width: 1200px;
    height: 1000px;
    overflow: hidden;
    background: var(--page);
  }
  .sign {
    position: absolute;
    left: 285px;
    top: 342px;
    width: 630px;
    height: 315px;
    box-sizing: border-box;
    border: 1px solid var(--ink);
    background: var(--white);
    overflow: hidden;
  }
  .sign__art {
    position: absolute;
    left: 0;
    top: 0;
    width: 630px;
    height: 188px;
  }
  .sign__brand {
    position: absolute;
    left: 0;
    top: 0;
    width: 360px;
    height: 188px;
    display: flex;
    align-items: center;
    justify-content: center;
    font-family: "Arimo", Arial, sans-serif;
    font-weight: 700;
    font-size: 40px;
    color: var(--ink);
    letter-spacing: 0.5px;
  }
  .services {
    position: absolute;
    left: 403px;
    top: 12px;
    margin: 0;
    padding: 0;
    list-style: none;
    font-family: "Arimo", Arial, sans-serif;
    font-weight: 700;
    font-size: 38px;
    line-height: 57.5px;
    color: var(--ink);
  }
  .services li {
    display: flex;
    align-items: center;
  }
  .services svg {
    width: 24px;
    height: 18px;
    margin-right: 4px;
  }
  .sign__name {
    position: absolute;
    left: 0;
    top: 188px;
    width: 100%;
    height: 85px;
    background: var(--slate);
    color: var(--white);
    font-family: "Roboto Condensed", "Arial Narrow", sans-serif;
    font-weight: 700;
    font-size: 46px;
    display: flex;
    align-items: center;
    justify-content: center;
  }
  .sign__phone {
    position: absolute;
    left: 0;
    top: 273px;
    width: 100%;
    height: 42px;
    background: var(--ink);
    color: var(--white);
    font-family: "Arimo", Arial, sans-serif;
    font-weight: 700;
    font-size: 24px;
    display: flex;
    align-items: center;
    justify-content: center;
  }
</style>
</head>
<body>
  <div class="sign">
    <svg class="sign__art" viewBox="0 0 630 188" aria-hidden="true">
      <path fill="var(--lime)" d="M0,0 H375 C340,40 330,72 345,110 C356,140 375,160 378,188 H0 Z"/>
      <path fill="var(--ink)" d="M375,0 H397 C356,45 342,76 356,114 C366,140 383,165 386,188 H378 C375,160 356,140 345,110 C330,72 340,40 375,0 Z"/>
    </svg>
    <div class="sign__brand">Bright Paws</div>
    <ul class="services">
      <li><svg viewBox="0 0 24 18"><path d="M0,0 L24,9 L0,18 L6,9 Z" fill="var(--ink)"/></svg>Daycare</li>
      <li><svg viewBox="0 0 24 18"><path d="M0,0 L24,9 L0,18 L6,9 Z" fill="var(--ink)"/></svg>Boarding</li>
      <li><svg viewBox="0 0 24 18"><path d="M0,0 L24,9 L0,18 L6,9 Z" fill="var(--ink)"/></svg>Learning</li>
    </ul>
    <div class="sign__name">Hound Play Lodge LLC</div>
    <div class="sign__phone">PHONE : 319-555-0187</div>
  </div>
</body>
</html>
```